Revolutionary Digital Car Parking Ticket

We are looking for a Brochure Type Web design and a design for a Logo for a brand new company and a product that has no equal anywhere in the world. The product is subject to a Patent Application.
The Company is Bellwether Kerbside Limited and will have a URL of www.lonmeroto.com.au
The designs need to be in Adobe Photo Shop and we are seeking the actual adobe file with unmerged layers.
The product is a digital parking ticket which automatically identifies where a car is parked and if applicable automatically bills the user of the device for the cost of parking for the time the vehicle is parked. The user no longer needs to worry about parking fines, or “feeding” the parking metre. Equally there is no longer any need for those ugly street parking metres.
A picture of the device is attached.
The design needs to impart to the user of the Web Site a feeling of a company which is innovative, designing cutting edge technology, very smart, friendly and sensitive to peoples needs in its area of technology development.
Equally the site needs to be:
a) very simple, uncluttered and clean;
b) such that any user intuitively understands how to use and get what they want.
c) such that the user again intuitively trust the product and the company to deliver a product which does what it indicates it can do;
d) such that it provides confidence that the use of the product will save them money and make sure they don’t get parking fines again and are only charged for the time that they are parked; and
e) such that all understand that they are in control of the operation of the product.
The front page of the Web site needs to provide the user with the following access points:
a) Buy a product;
b) Log into their established account;
c) Make contact with the company;
d) Understand all of the Company Privacy Conditions; and
e) Understand who the company is.
Updates
Please remember that the product is about car parking in any place and one needs to ensure that a site user immediately recognises that by buying the device it makes Car Parking much easier. To put this another way the graphics on the site need to immediately let the user know we are on about car parking made easy.
Target Market(s)
Consumers. Ordinary people who drive cars
Industry/Entity Type
Digital
Logo Text
Ever Calm Tidy Motoring
Number of Pages Required
1 page
Font styles to use
Requirements
Must have
- Must be simple and clean and uncluttered
Nice to have
- Nil
Should not have
- Must not be cluttered

```html
<!DOCTYPE html>
<html lang="en">
<head>
<meta charset="utf-8">
<title>Tidyway — Ever Calm Tidy Motoring</title>
<link href="https://fonts.googleapis.com/css2?family=Montserrat:wght@400;600;700;800&family=Open+Sans:wght@400;600;700&display=swap" rel="stylesheet">
<style>
:root{
  --yellow:#fdb913;
  --yellow-dark:#e9a800;
  --ink:#222222;
  --text:#555555;
  --muted:#8a8a8a;
  --line:#dddddd;
  --white:#ffffff;
  --dark:#2b2b2b;
  --hero-a:#3a3d42;
  --hero-b:#16181b;
}
*{box-sizing:border-box;margin:0;padding:0}
html,body{width:1200px;height:3056px;overflow:hidden}
body{font-family:"Open Sans",Arial,sans-serif;color:var(--text);background:var(--white);font-size:13px;line-height:1.5}
.heading{font-family:"Montserrat",Arial,sans-serif;font-weight:800;color:var(--ink);text-transform:uppercase;letter-spacing:.5px;white-space:nowrap}
.btn{display:inline-block;font-family:"Montserrat",Arial,sans-serif;font-size:11px;font-weight:600;padding:7px 20px;border-radius:2px;color:var(--white);background:var(--yellow);white-space:nowrap;text-align:center}
.btn-dark{background:var(--dark)}

/* header */
.site-header{height:56px;display:flex;align-items:center;padding:0 70px;position:relative;z-index:2;background:var(--white)}
.brand{display:flex;align-items:center;gap:8px;font-family:"Montserrat",Arial,sans-serif;font-weight:800;font-size:26px;color:var(--ink)}
.brand-dot{width:14px;height:14px;background:var(--yellow);border-radius:50%}
.main-nav{margin-left:auto;display:flex;align-items:center;gap:30px;font-family:"Montserrat",Arial,sans-serif;font-size:11px;font-weight:600;color:var(--ink)}
.cart{margin-left:10px;width:96px}
.search{width:120px;height:22px;border:1px solid var(--line);border-radius:2px;margin-left:14px;position:relative}
.search::after{content:"";position:absolute;right:6px;top:5px;width:8px;height:8px;border:2px solid var(--muted);border-radius:50%}

/* hero */
.hero{position:relative;height:574px;background:linear-gradient(160deg,var(--hero-a),var(--hero-b) 70%)}
.hero-photo{position:absolute;inset:0;background:linear-gradient(100deg,rgba(20,20,22,.9) 0%,rgba(80,84,90,.55) 55%,rgba(150,154,160,.5) 100%)}
.hero-copy{position:absolute;left:70px;top:188px;width:420px}
.hero-copy h1{font-family:"Montserrat",Arial,sans-serif;font-weight:800;font-size:34px;line-height:1.08;text-transform:uppercase;color:var(--white);margin-bottom:12px}
.hero-copy h1 span{color:var(--yellow)}
.hero-copy p{color:var(--white);font-size:13px;margin-bottom:18px}
.login{position:absolute;left:842px;top:228px;width:268px;height:190px;background:rgba(255,255,255,.88);padding:18px 22px}
.login h2{font-family:"Montserrat",Arial,sans-serif;font-size:20px;color:var(--ink);margin-bottom:10px}
.field{height:24px;border:1px solid var(--line);background:var(--white);font-size:10px;color:var(--muted);padding:4px 8px;margin-bottom:8px}
.login .btn{margin-top:8px;margin-left:auto;display:block;width:120px;padding:7px 0}
.dots{position:absolute;left:0;right:0;top:520px;display:flex;justify-content:center;gap:10px}
.dots i{width:12px;height:12px;border-radius:50%;border:2px solid var(--white)}
.dots i.on{background:var(--yellow);border-color:var(--yellow)}

/* product */
.product{height:510px;padding:64px 70px 0}
.section-head{display:flex;align-items:center;gap:200px;margin-bottom:26px}
.section-head .heading{font-size:30px;width:310px}
.rule{height:1px;background:var(--line)}
.product-row{display:flex;gap:54px;padding:40px 25px 24px}
.product-image{width:156px;height:200px;background:linear-gradient(180deg,#eeeeee,#c9c9c9)}
.product-info{width:380px;font-size:12px}
.product-info h3{font-family:"Montserrat",Arial,sans-serif;font-size:16px;color:var(--ink)}
.price{font-weight:700;color:var(--ink)}
.stock{color:var(--muted);font-size:11px;margin-bottom:14px}
.product-info h4{font-size:12px;color:var(--ink);margin-bottom:2px}
.product-info p{margin-bottom:16px}

/* about */
.about{height:514px;background:var(--yellow);padding:70px 70px 0}
.about .section-head .heading{width:auto}
.about .section-head{gap:94px}
.cards{display:grid;grid-template-columns:1fr 1fr;gap:6px;background:var(--white);padding:6px;margin-top:28px}
.card{display:flex;gap:22px;align-items:center;padding:22px 24px;background:var(--white);border:1px solid var(--line);height:136px}
.avatar{flex:none;width:88px;height:88px;border-radius:50%;background:linear-gradient(135deg,#b9a99a,#6b5d52)}
.card h3{font-family:"Montserrat",Arial,sans-serif;font-size:15px;color:var(--ink)}
.card p{font-size:12px}
.more{color:var(--yellow-dark);font-size:11px;font-weight:600}

/* videos */
.videos{height:540px;padding:66px 70px 0}
.videos .section-head .heading{width:auto;font-size:30px}
.videos .section-head{gap:62px}
.video-row{display:flex;gap:12px}
.video{width:524px}
.thumb{height:280px;position:relative;background:linear-gradient(180deg,#6e7176,#2e3033)}
.thumb.garage{background:linear-gradient(180deg,#585a5e,#8d8f92)}
.video h3{font-size:13px;color:var(--yellow-dark);font-weight:600;margin-top:8px}
.video .by{font-size:11px;color:var(--muted)}
.progress{height:14px;background:#e6e6e6;margin-top:26px}
.progress span{display:block;width:30%;height:100%;background:var(--yellow)}

/* benefits & testimonials */
.split{height:592px;background:var(--yellow);display:flex;padding:0 70px}
.benefits{width:520px;padding-top:80px}
.benefits .heading{font-size:30px;margin-bottom:24px}
.benefits p{color:var(--white);font-size:12px;width:440px;margin-bottom:40px}
.benefits .btn{margin-left:170px}
.testimonials{width:540px;padding-top:80px}
.testimonials .head{display:flex;justify-content:space-between;align-items:center;margin-bottom:20px}
.testimonials .heading{font-size:30px}
.quote{background:var(--white);display:flex;gap:20px;padding:22px;height:150px;border-bottom:1px solid var(--line)}
.quote .avatar{width:80px;height:80px}
.quote h3{font-size:14px;color:var(--yellow-dark);font-weight:600}
.quote p{font-size:12px}

/* footer */
.site-footer{height:226px;padding:40px 70px 0;display:flex;gap:70px;font-size:10px;position:relative}
.site-footer h4{font-family:"Montserrat",Arial,sans-serif;font-size:11px;color:var(--ink);margin-bottom:8px}
.site-footer li{list-style:none;line-height:1.7}
.col{width:190px}
.social{display:flex;gap:8px;margin-bottom:20px}
.social i{width:16px;height:16px;border-radius:50%;background:var(--yellow)}
.news{display:flex;margin-top:6px}
.news span{flex:1;border:1px solid var(--line);height:20px}
.news b{background:var(--yellow);color:var(--white);padding:3px 10px;font-weight:600}
.tweet{margin-bottom:8px}
.tweet strong{color:var(--yellow-dark)}
.site-footer .brand{position:absolute;left:70px;bottom:34px}
.bottom-bar{height:34px;background:var(--dark);border-top:4px solid var(--yellow);color:var(--white);font-size:10px;text-align:center;line-height:30px}
</style>
</head>
<body>
<header class="site-header">
  <div class="brand"><span class="brand-dot"></span>Tidyway</div>
  <nav class="main-nav">
    <span>HOME</span><span>ABOUT US</span><span>PRODUCT</span><span>MY ACCOUNT</span><span>FAQ</span>
    <span class="btn cart">My Cart</span>
    <span class="search"></span>
  </nav>
</header>

<section class="hero">
  <div class="hero-photo" role="img" aria-label="Parking lot with a silver hatchback parked in a marked bay"></div>
  <div class="hero-copy">
    <h1>Sed ut perspiciatis <span>unde omnis iste natus error</span></h1>
    <p>Lorem ipsum dolor sit amet, consectetur adipiscing elit, sed do eiusmod tempor incididunt ut labore dolore magna aliqua.</p>
    <span class="btn">Read more</span>
  </div>
  <form class="login">
    <h2>Login</h2>
    <div class="field">Username</div>
    <div class="field">Password</div>
    <span class="btn">Submit Login</span>
  </form>
  <div class="dots"><i></i><i class="on"></i><i></i></div>
</section>

<section class="product">
  <div class="section-head"><h2 class="heading">Our Product</h2><span class="btn">Shop All</span></div>
  <div class="rule"></div>
  <div class="product-row">
    <div class="product-image" role="img" aria-label="Digital parking ticket device"></div>
    <div class="product-info">
      <h3>Tidyway</h3>
      <div class="price">$ 49.00</div>
      <div class="stock">In Stock | Free Shipping</div>
      <h4>Advantages of Tidyway</h4>
      <p>Contrary to popular belief, Lorem Ipsum is not simply random text. It has roots in a piece of classical Latin literature from 45 BC, making it over 2000 years old. A professor at a college in Virginia looked up one of the more obscure Latin words.</p>
      <span class="btn">Add to cart</span>
    </div>
  </div>
  <div class="rule"></div>
</section>

<section class="about">
  <div class="section-head"><h2 class="heading">About Us</h2><span class="btn btn-dark">Read All</span></div>
  <div class="cards">
    <article class="card"><div class="avatar" role="img" aria-label="Company photo"></div><div><h3>Company</h3><p>Sed ut perspiciatis unde omnis iste natus error sit voluptatem accusantium doloremque laudantium, totam rem aperiam.</p><span class="more">Read more</span></div></article>
    <article class="card"><div class="avatar" role="img" aria-label="Team member portrait"></div><div><h3>Our Team</h3><p>Sed ut perspiciatis unde omnis iste natus error sit voluptatem accusantium doloremque laudantium, totam rem aperiam.</p><span class="more">Read more</span></div></article>
    <article class="card"><div class="avatar" role="img" aria-label="Vision portrait"></div><div><h3>Our Vision</h3><p>Sed ut perspiciatis unde omnis iste natus error sit voluptatem accusantium doloremque laudantium, totam rem aperiam.</p><span class="more">Read more</span></div></article>
    <article class="card"><div class="avatar" role="img" aria-label="Founder portrait"></div><div><h3>Our Establishment</h3><p>Sed ut perspiciatis unde omnis iste natus error sit voluptatem accusantium doloremque laudantium, totam rem aperiam.</p><span class="more">Read more</span></div></article>
  </div>
</section>

<section class="videos">
  <div class="section-head"><h2 class="heading">Tidyway Videos</h2><span class="btn">Shop all</span></div>
  <div class="video-row">
    <div class="video"><div class="thumb" role="img" aria-label="Car parked beside a kerb-side parking bay"></div><h3>Education is important</h3><div class="by">By Marlo Vence</div></div>
    <div class="video"><div class="thumb garage" role="img" aria-label="Entrance to a multi-level car park"></div><h3>Why Tidyway?</h3><div class="by">By Corin Dale</div></div>
  </div>
  <div class="progress"><span></span></div>
</section>

<section class="split">
  <div class="benefits">
    <h2 class="heading">Benefits</h2>
    <p>Lorem ipsum dolor sit amet, consectetur adipiscing elit, sed do eiusmod tempor incididunt ut labore et dolore magna aliqua. Ut enim ad minim veniam, quis nostrud exercitation ullamco laboris nisi ut aliquip ex ea commodo consequat. Duis aute irure dolor in reprehenderit in voluptate velit esse cillum dolore eu fugiat nulla pariatur. Excepteur sint occaecat cupidatat non proident, sunt in culpa qui officia deserunt mollit anim id est laborum.</p>
    <span class="btn btn-dark">See more</span>
  </div>
  <div class="testimonials">
    <div class="head"><h2 class="heading">User Testimonials</h2><span class="btn btn-dark">Read All</span></div>
    <div class="quote"><div class="avatar" role="img" aria-label="Customer portrait"></div><div><h3>Sed ut perspiciatis</h3><p>Sed ut perspiciatis unde omnis iste natus error sit voluptatem accusantium doloremque laudantium, totam rem aperiam.</p><span class="more">By Corin Dale</span></div></div>
    <div class="quote"><div class="avatar" role="img" aria-label="Customer portrait"></div><div><h3>Sed ut perspiciatis</h3><p>Sed ut perspiciatis unde omnis iste natus error sit voluptatem accusantium doloremque laudantium, totam rem aperiam.</p><span class="more">By Marlo Vence</span></div></div>
  </div>
</section>

<footer class="site-footer">
  <div class="col"><h4>SITEMAP</h4><ul><li>Home</li><li>About Us</li><li>My Account</li><li>FAQ</li><li>Products</li></ul></div>
  <div class="col"><h4>LINKS</h4><ul><li>Blog</li><li>Terms and Conditions</li><li>Privacy Policy</li><li>Product News</li><li>Contact Us</li></ul></div>
  <div class="col"><h4>FOLLOW US</h4><div class="social"><i></i><i></i><i></i><i></i><i></i></div><h4>JOIN OUR NEWSLETTER</h4><div class="news"><span></span><b>Subscribe</b></div></div>
  <div class="col"><h4>RECENT TWEETS</h4><p class="tweet"><strong>@tidyway</strong> Parking made calm and easy, lorem ipsum dolor sit.</p><p class="tweet"><strong>@tidyway</strong> No more fines, lorem ipsum amet consectetur.</p></div>
  <div class="brand"><span class="brand-dot"></span>Tidyway</div>
</footer>
<div class="bottom-bar">© Tidyway. All rights reserved.</div>
</body>
</html>
```